Surface Protection company needs cards

We are a New Zealand company that will apply nanotechnology coatings on surfaces to prevent growth and spread of bacteria, viruses, mold etc with a sprayer. We deal with large corporates, airlines, hospitals and schools so we are after a new modern, simple and clean look that will have great visual impact.
We a company that is focused on prevention and protection.

Company name, Vela Shield

Subtext, Antimicrobial Surface Protection

Logo, VS

Target Market(s)

Hospitals, Transport agencies, Airlines, Corporate entities

Contact Information for Business Card

Company name, VelaShield
Logo, VS

Gareth Tolley
velashieldnz@postbox.example
+64219305562
www.velashield.example.nz

Requirements
Must have
• Simple clean look.
Nice to have
• We apply nano coatings so try and incorporate this into a theme somehow

```html
<!DOCTYPE html>
<html lang="en">
<head>
<meta charset="utf-8">
<title>Vela Shield – Business Cards</title>
<link rel="stylesheet" href="https://fonts.googleapis.com/css2?family=Arimo:wght@400&display=swap">
<style>
  :root {
    --backdrop: #2b2828;
    --card-white: #ffffff;
    --brand-blue: #2aa9e2;
    --brand-blue-deep: #1f8fd0;
    --brand-navy: #1c1f4d;
    --ink: #111111;
    --on-blue: #ffffff;
  }
  * { margin: 0; padding: 0; box-sizing: border-box; }
  html, body {
    width: 1200px;
    height: 1200px;
    overflow: hidden;
    background: var(--backdrop);
    font-family: "Arimo", Arial, sans-serif;
  }
  .card {
    position: absolute;
    left: 246px;
    width: 710px;
    height: 403px;
    border-radius: 26px;
    overflow: hidden;
  }
  .card--front { top: 164px; background: var(--card-white); }
  .card--back { top: 637px; }

  .front__brand-panel {
    position: absolute;
    left: 0; top: 0;
    width: 305px; height: 100%;
    display: flex;
    align-items: center;
    justify-content: center;
  }
  .brand-mark {
    font-size: 62px;
    font-weight: 400;
    color: var(--brand-navy);
    letter-spacing: 1px;
    line-height: 1;
  }
  .wave-field {
    position: absolute;
    background: linear-gradient(135deg, var(--brand-blue) 0%, var(--brand-blue) 55%, var(--brand-blue-deep) 100%);
  }
  .front__info-panel {
    position: absolute;
    left: 305px; top: 0;
    width: 405px; height: 100%;
  }
  .front__info-panel .wave-field { inset: 0; }

  .company-name {
    position: absolute;
    left: 0; width: 100%;
    top: 106px;
    text-align: center;
    font-size: 26px;
    color: var(--ink);
    padding-left: 57px;
    padding-right: 0;
  }
  .company-tagline {
    position: absolute;
    left: 0; width: 100%;
    top: 143px;
    text-align: center;
    font-size: 15px;
    color: var(--ink);
    padding-left: 57px;
  }
  .person-name {
    position: absolute;
    left: 99px;
    top: 197px;
    font-size: 24px;
    color: var(--ink);
  }
  .contact-list {
    position: absolute;
    left: 65px;
    top: 243px;
    list-style: none;
  }
  .contact-list li {
    display: flex;
    align-items: center;
    height: 32px;
    color: var(--ink);
    font-size: 18px;
  }
  .contact-list li.contact--phone { font-size: 23px; height: 36px; }
  .contact-icon {
    width: 22px; height: 22px;
    margin-right: 12px;
    flex: none;
  }

  .card--back .wave-field { inset: 0; }
  .back__content {
    position: absolute;
    inset: 0;
    display: flex;
    flex-direction: column;
    align-items: center;
    padding-top: 132px;
  }
  .brand-mark--large {
    font-size: 88px;
    color: var(--on-blue);
  }
  .back__web {
    margin-top: 30px;
    font-size: 18px;
    color: var(--on-blue);
  }
</style>
</head>
<body>

<section class="card card--front" aria-label="Business card front">
  <div class="front__brand-panel">
    <span class="brand-mark">VS</span>
  </div>
  <div class="front__info-panel">
    <div class="wave-field" role="img" aria-label="Flowing blue spray waves representing nano coating"></div>
    <h1 class="company-name">Vela Shield</h1>
    <p class="company-tagline">Antimicrobial Surface Protection</p>
    <p class="person-name">Gareth Tolley</p>
    <ul class="contact-list">
      <li class="contact--phone">
        <svg class="contact-icon" viewBox="0 0 24 24" aria-hidden="true">
          <path fill="#fff" d="M6.6 3.5l2.6 3.3-1.6 2c1 2.3 2.9 4.3 5.3 5.5l2-1.6 3.3 2.5-1.3 3c-6.5.3-12.7-6-12.4-12.4z"/>
        </svg>
        +64219305562
      </li>
      <li>
        <svg class="contact-icon" viewBox="0 0 24 24" aria-hidden="true">
          <rect x="3" y="7" width="18" height="13" rx="1.5" fill="#fff"/>
          <path d="M3.5 8l8.5 6 8.5-6" fill="none" stroke="#2aa9e2" stroke-width="1.6"/>
        </svg>
        velashieldnz@postbox.example
      </li>
      <li>
        <svg class="contact-icon" viewBox="0 0 24 24" aria-hidden="true">
          <g fill="none" stroke="#fff" stroke-width="1.6">
            <circle cx="12" cy="12" r="8.5"/>
            <ellipse cx="12" cy="12" rx="3.8" ry="8.5"/>
            <path d="M3.5 12h17M5 7.5h14M5 16.5h14"/>
          </g>
        </svg>
        www.velashield.example.nz
      </li>
    </ul>
  </div>
</section>

<section class="card card--back" aria-label="Business card back">
  <div class="wave-field" role="img" aria-label="Swirling blue spray waves representing nano coating"></div>
  <div class="back__content">
    <span class="brand-mark brand-mark--large">VS</span>
    <p class="back__web">www.velashield.example.nz</p>
  </div>
</section>

</body>
</html>
```